Business card design

Hi,
I need to have a business card design based on the current logo.
If competitive I not put it out to everyone.

It can be single of double sided

Target Market(s)

Food businesses

Industry/Entity Type

Food Manufacturing

Contact Information for Business Card

Details will on card will be as follows Name = Marcus Helt Email = Marcus@TalBakery.com.au Phone = 0418562207 Address = 17 Lanford Street , Fortitude Valley QLD 4006 Australia

Font styles to use
Other font styles liked:
• based on two fonts - Adelle & Museo

Requirements
Must have
• Based on the on switch concept

```html
<!DOCTYPE html>
<html lang="en">
<head>
<meta charset="utf-8">
<title>TalBakery Business Card</title>
<link href="https://fonts.googleapis.com/css2?family=Quicksand:wght@500;700&display=swap" rel="stylesheet">
<style>
  :root {
    --bg: #2b2b2d;
    --red: #e2234a;
    --red-deep: #d0213f;
    --brown: #3a2328;
    --ink: #3b2a2d;
    --paper: #ffffff;
    --paper-shade: #ececec;
  }
  * { margin: 0; padding: 0; box-sizing: border-box; }
  html, body { width: 1200px; height: 900px; overflow: hidden; }
  body {
    background: var(--bg);
    font-family: "Quicksand", sans-serif;
    position: relative;
  }
  .card {
    position: absolute;
    width: 640px;
    height: 370px;
    padding: 22px;
    box-shadow: 0 18px 40px rgba(0,0,0,0.45);
  }
  .card--front { left: 110px; top: 50px; background: var(--red); }
  .card--back { left: 450px; top: 480px; background: var(--brown); }
  .card__face {
    width: 100%; height: 100%;
    background: linear-gradient(135deg, var(--paper-shade), var(--paper) 70%);
    position: relative;
  }
  .brand {
    position: absolute;
    display: flex;
    align-items: center;
    gap: 14px;
  }
  .brand__dot {
    width: 46px; height: 46px; border-radius: 50%;
    background: var(--red-deep);
    flex: none;
  }
  .brand__name {
    font-family: "Quicksand", sans-serif;
    font-weight: 700;
    font-size: 60px;
    line-height: 1;
    color: var(--ink);
    letter-spacing: 1px;
  }
  .card--front .brand { left: 50%; top: 50%; transform: translate(-50%, -50%); }
  .card--back .brand { left: 50px; top: 64px; }
  .contact {
    position: absolute;
    left: 50px; top: 196px;
    display: flex;
    align-items: center;
  }
  .contact__name {
    font-weight: 700;
    font-size: 22px;
    color: var(--red);
    text-transform: uppercase;
    letter-spacing: 0.5px;
    padding-right: 22px;
    white-space: nowrap;
  }
  .contact__divider {
    width: 1px; height: 100px; background: var(--ink); flex: none;
  }
  .contact__list {
    list-style: none;
    padding-left: 20px;
    font-weight: 500;
    font-size: 15px;
    color: var(--ink);
  }
  .contact__item { display: flex; align-items: flex-start; gap: 9px; margin: 5px 0; line-height: 1.3; white-space: nowrap; }
  .contact__icon { width: 15px; height: 15px; flex: none; margin-top: 2px; fill: var(--red); }
</style>
</head>
<body>
  <section class="card card--front">
    <div class="card__face">
      <div class="brand">
        <span class="brand__dot"></span>
        <span class="brand__name">TalBakery</span>
      </div>
    </div>
  </section>

  <section class="card card--back">
    <div class="card__face">
      <div class="brand">
        <span class="brand__dot"></span>
        <span class="brand__name">TalBakery</span>
      </div>
      <div class="contact">
        <h1 class="contact__name">Marcus Helt</h1>
        <span class="contact__divider"></span>
        <ul class="contact__list">
          <li class="contact__item">
            <svg class="contact__icon" viewBox="0 0 24 24"><path d="M6.6 10.8a15 15 0 0 0 6.6 6.6l2.2-2.2c.3-.3.7-.4 1-.2 1.1.4 2.3.6 3.6.6.6 0 1 .4 1 1V20c0 .6-.4 1-1 1A17 17 0 0 1 3 4c0-.6.4-1 1-1h3.5c.6 0 1 .4 1 1 0 1.3.2 2.5.6 3.6.1.3 0 .7-.2 1z"/></svg>
            <span>0418562207</span>
          </li>
          <li class="contact__item">
            <svg class="contact__icon" viewBox="0 0 24 24"><path d="M2 5h20v14H2z M4 7v.5l8 5 8-5V7l-8 5z" fill-rule="evenodd"/></svg>
            <span>Marcus@TalBakery.com.au</span>
          </li>
          <li class="contact__item">
            <svg class="contact__icon" viewBox="0 0 24 24"><path d="M12 2a7 7 0 0 0-7 7c0 5 7 13 7 13s7-8 7-13a7 7 0 0 0-7-7zm0 9.5A2.5 2.5 0 1 1 12 6.5a2.5 2.5 0 0 1 0 5z"/></svg>
            <span>17 Lanford Street<br>Norwell Heights QLD 4125 Australia</span>
          </li>
        </ul>
      </div>
    </div>
  </section>
</body>
</html>
```